Sun Jubilee - Concert Poster

We need a poster for a concert involving 3 bands. Marmaduke, Auntie's Gumbo and Velveteen Ray. The event is called the Sun Jubilee. The poster will be a take away. We plan to print some to give out and some for advertising. Should be something people will want to put up on a wall. The poster should have a psychedelic "flavor", colorful.
Info. that needs to be on the poster: Sun Jubilee - Band Names - Pelham Brook's Music Hall - 4182 Route 17, Felton CA - $10 advance Tix - $12 at Door - for tickets www.pelhambrookmusic. - 21 and Over - March 21 2015 - Doors open at 7:00.

Industry/Entity Type

Event

```html
<!DOCTYPE html>
<html lang="en">
<head>
<meta charset="utf-8">
<title>Sun Jubilee – Concert Poster</title>
<link rel="stylesheet" href="https://fonts.googleapis.com/css2?family=Audiowide&family=Michroma&family=Open+Sans:wght@300;400;600;700&display=swap">
<style>
  :root {
    --paper: #ffffff;
    --night: #050507;
    --ember: #e8452a;
    --ember-band: rgba(214, 62, 48, 0.82);
    --violet: #4a2a78;
    --gold-glow: #ffb23a;
    --blue-glow: #7fb6ff;
    --door-amber: #f2a43a;
  }
  * { margin: 0; padding: 0; box-sizing: border-box; }
  html, body { width: 792px; height: 1200px; overflow: hidden; background: var(--paper); }
  .poster {
    position: relative;
    width: 792px; height: 1200px;
    overflow: hidden;
    background: var(--paper);
    font-family: "Open Sans", Arial, sans-serif;
  }
  .artwork {
    position: absolute;
    left: 20px; top: 18px; width: 752px; height: 1162px;
    background:
      radial-gradient(ellipse 260px 220px at 560px 620px, rgba(220,215,245,0.85), transparent 70%),
      radial-gradient(ellipse 320px 260px at 180px 820px, rgba(120,30,60,0.55), transparent 70%),
      radial-gradient(ellipse 400px 300px at 380px 1050px, rgba(90,40,140,0.6), transparent 70%),
      linear-gradient(180deg, var(--night) 0%, #140a10 22%, #3a1626 40%, var(--violet) 62%, #2a1840 82%, #1a0f22 100%);
    overflow: hidden;
  }
  .title {
    position: absolute;
    font-family: "Audiowide", sans-serif;
    font-weight: 400;
    color: var(--paper);
    line-height: 1;
    letter-spacing: 2px;
    white-space: nowrap;
  }
  .title--first {
    left: 110px; top: 62px;
    font-size: 120px;
    text-shadow: 0 0 6px var(--blue-glow), 0 0 16px rgba(255,160,80,0.8), 0 0 26px rgba(255,120,60,0.45);
  }
  .title--second {
    right: 90px; top: 212px;
    font-size: 104px;
    text-align: right;
    text-shadow: 0 0 6px var(--gold-glow), 0 0 16px rgba(255,190,60,0.85), 0 0 26px rgba(255,140,40,0.45);
  }
  .featuring {
    position: absolute; left: 0; right: 0; top: 400px;
    text-align: center; color: var(--paper);
    font-weight: 300; font-size: 28px;
  }
  .lineup {
    position: absolute; left: 0; right: 0; top: 478px;
    text-align: center;
    font-family: "Michroma", sans-serif;
    font-weight: 400;
    color: var(--ember);
    font-size: 42px; line-height: 70px;
    letter-spacing: 3px;
    -webkit-text-stroke: 2px var(--paper);
    paint-order: stroke fill;
    text-transform: uppercase;
    white-space: nowrap;
  }
  .band { display: block; }
  .band--headline { font-size: 50px; }
  .date-band {
    position: absolute; left: 404px; top: 758px; width: 368px; height: 48px;
    background: var(--ember-band);
    color: var(--paper); font-weight: 700; font-size: 29px;
    line-height: 48px; padding-left: 24px;
    text-shadow: 0 1px 3px rgba(0,0,0,0.5);
  }
  .venue-band {
    position: absolute; left: 20px; top: 852px; width: 600px; height: 94px;
    background: var(--ember-band);
    color: var(--paper); font-size: 27px; line-height: 33px;
    padding: 14px 0 0 60px;
    text-shadow: 0 1px 3px rgba(0,0,0,0.5);
  }
  .price-band {
    position: absolute; left: 20px; top: 985px; width: 752px; height: 48px;
    background: var(--night);
    color: var(--paper); font-size: 30px; line-height: 48px;
    text-align: center;
  }
  .tickets {
    position: absolute; left: 0; right: 0; top: 1062px;
    text-align: center; color: var(--ember); font-size: 24px;
  }
  .doors {
    position: absolute; left: 0; right: 0; top: 1124px;
    text-align: center; color: var(--door-amber); font-size: 13px;
  }
</style>
</head>
<body>
<main class="poster">
  <div class="artwork" role="img" aria-label="Abstract psychedelic burst of shattered red, purple and lilac shards on black"></div>

  <h1 class="title title--first">Sun</h1>
  <p class="title title--second">Jubilee</p>

  <p class="featuring">-Featuring-</p>

  <h2 class="lineup">
    <span class="band band--headline">Marmaduke</span>
    <span class="band">Auntie's Gumbo</span>
    <span class="band">&amp; Velveteen Ray</span>
  </h2>

  <p class="date-band">on 21st March 2015</p>

  <p class="venue-band">At Pelham Brook's Music Hall - 4182<br>Route 17, Felton CA . 21+</p>

  <p class="price-band">$10 advance Tix &nbsp;- &nbsp;$12 at Door</p>

  <p class="tickets">For tickets- www.pelhambrookmusic.info</p>

  <p class="doors">Doors open at 7:00</p>
</main>
</body>
</html>
```